Create a Graphic About YOURSELF and PixelHarbor

PixelHarbor would like you (designers) to create an awesome graphic to promote YOURSELF and your profile on PixelHarbor!

Your graphic should communicate your name, your services and should mention PixelHarbor.

The design should be perfect for sharing on Chatterly. Here's an example of what we'd like http://blog.pixelharbor-example.ca/article/333/pixelharbor-launches-3000-hire-me-social-design-contest

Once you submitted your design, we'd love you to share the design ('advertisement') and promote yourself and PixelHarbor to your friends and potential customers. So make your submissions great and get your friends to vote for your design by 'Liking' it on Chatterly!

Prizes:
$1500 - "PixelHarbor Community" prize awarded to the designer with the most Chatterly 'Likes'
5 x $50 for the next 5 'most liked' designs on Chatterly

$1000 - "Hire Me" prize awarded to the designer who receives the most client invites
5 x $50 for the next 5 'most invited' designers

In summary, this is a great opportunity for you to increase your exposure to PixelHarbor customers and win cash prizes. Show off your design skills and get hired by PixelHarbor customers from around the world!

Target Market(s)

Fans, friends and customers of YOU

Industry/Entity Type

Cash

Requirements
Must have
• 1) Include your PixelHarbor user name on the graphic so customers can find you in the PixelHarbor Designer Directory
2) Include the tagline "Hire Me on PixelHarbor.com!" in your graphic design.
3) Share your design's URL on our Chatterly wall at http://chatterly-example.com/pixelharbor and get your friends to 'like' your design.
Nice to have
• 1) Include a tagline that expresses your design approach/philosophy
2) Artwork dimensions: 403 x 403 px
3) You can submit more than 1 design!
Should not have
• You must own the copyright of any images you use including stock imagery.

```html
<!DOCTYPE html>
<html lang="en">
<head>
<meta charset="utf-8">
<title>What I Offer – Ardi Wirasena</title>
<link rel="stylesheet" href="https://fonts.googleapis.com/css2?family=Nothing+You+Could+Do&display=swap">
<style>
  :root {
    --paper-light: #f3efe6;
    --paper-mid: #e8e1d2;
    --paper-edge: #cfc4ad;
    --ink: #3a2418;
    --accent-red: #b81e22;
  }
  html, body {
    margin: 0;
    padding: 0;
    width: 1200px;
    height: 678px;
    overflow: hidden;
  }
  .offer-board {
    position: relative;
    width: 1200px;
    height: 678px;
    background: radial-gradient(ellipse at 50% 45%, var(--paper-light) 0%, var(--paper-mid) 60%, var(--paper-edge) 100%);
  }
  .offer-map {
    position: absolute;
    inset: 0;
    width: 1200px;
    height: 678px;
  }
  .hand-text {
    font-family: "Nothing You Could Do", cursive;
    fill: var(--ink);
    stroke: var(--ink);
    stroke-width: 0.8;
  }
  .title-text { font-size: 50px; stroke-width: 1.4; }
  .name-text { font-size: 50px; }
  .service-text { font-size: 44px; }
  .hire-text { font-size: 28px; }
  .user-text { font-size: 24px; }
  .ink-line {
    fill: none;
    stroke: var(--ink);
    stroke-width: 3;
    stroke-linecap: round;
  }
  .ink-loop {
    fill: none;
    stroke: var(--ink);
    stroke-width: 3.5;
    stroke-linecap: round;
  }
  .red-mark {
    fill: none;
    stroke: var(--accent-red);
    stroke-width: 3;
    stroke-linecap: round;
  }
</style>
</head>
<body>
<main class="offer-board">
  <svg class="offer-map" viewBox="0 0 1200 678" xmlns="http://www.w3.org/2000/svg">
    <g class="heading">
      <text class="hand-text title-text" x="576" y="82" text-anchor="middle">What I Offer</text>
      <path class="red-mark" d="M420 104 Q580 96 738 102"/>
      <path class="ink-line" d="M455 110 Q600 104 705 108" stroke-width="2"/>
    </g>

    <g class="hire-me">
      <text class="hand-text hire-text" x="1172" y="92" text-anchor="end">Hire Me on</text>
      <text class="hand-text hire-text" x="1172" y="130" text-anchor="end">PixelHarbor.com!</text>
      <path class="red-mark" d="M945 142 Q1060 136 1178 140"/>
      <text class="hand-text user-text" x="1172" y="178" text-anchor="end">@ardiwirasena</text>
    </g>

    <g class="connectors">
      <path class="ink-line" d="M470 300 Q360 310 230 330"/>
      <path class="ink-line" d="M520 335 Q380 400 260 480"/>
      <path class="ink-line" d="M570 345 Q545 420 530 476"/>
      <path class="ink-line" d="M660 355 Q650 480 700 560 Q760 600 840 596"/>
      <path class="ink-line" d="M700 350 Q750 420 825 480"/>
      <path class="ink-line" d="M780 320 Q850 360 880 410"/>
      <path class="ink-line" d="M560 390 L760 330" stroke-width="1.5"/>
      <path class="ink-line" d="M610 355 L612 368" stroke-width="2"/>
    </g>

    <g class="center-node">
      <ellipse class="ink-loop" cx="618" cy="272" rx="228" ry="62" transform="rotate(-3 618 272)"/>
      <ellipse class="ink-loop" cx="614" cy="270" rx="220" ry="56" transform="rotate(2 614 270)"/>
      <ellipse class="ink-loop" cx="620" cy="275" rx="234" ry="66" transform="rotate(-1 620 275)" stroke-width="2.5"/>
      <ellipse class="red-mark" cx="616" cy="272" rx="226" ry="60" transform="rotate(1 616 272)"/>
      <text class="hand-text name-text" x="615" y="288" text-anchor="middle">Ardi Wirasena</text>
    </g>

    <g class="service service-vector">
      <ellipse class="red-mark" cx="76" cy="334" rx="26" ry="30"/>
      <text class="hand-text service-text" x="60" y="352">Vectorly</text>
      <path class="red-mark" d="M40 362 Q180 350 300 358"/>
    </g>

    <g class="service service-pixel">
      <ellipse class="red-mark" cx="332" cy="502" rx="70" ry="38"/>
      <text class="hand-text service-text" x="130" y="518">PixelForge</text>
    </g>

    <g class="service service-page">
      <ellipse class="red-mark" cx="556" cy="512" rx="116" ry="38"/>
      <text class="hand-text service-text" x="455" y="527">PageCraft</text>
    </g>

    <g class="service service-site">
      <text class="hand-text service-text" x="880" y="442">SiteBloom</text>
      <path class="red-mark" d="M870 450 Q1000 446 1130 442"/>
    </g>

    <g class="service service-logo">
      <text class="hand-text service-text" x="825" y="518">LoGo</text>
      <path class="red-mark" d="M800 530 Q880 524 968 528"/>
    </g>

    <g class="service service-promo">
      <text class="hand-text service-text" x="845" y="596">Promotion Items</text>
      <path class="red-mark" d="M838 612 Q1000 604 1180 610"/>
    </g>
  </svg>
</main>
</body>
</html>
```